CD cover "Marisol Quintero"

Here I send the pictures for the cover, leaving creative freedom to the photography and any modifications you make. The artist is called Marisol Quintero, and the title of the album is called. "Over Quiet Rivers" but please translate that to Spanish. Thank you for your valuable work.
The name of the artist is: Marisol Quintero
Album Name: “Sobre ríos quietos” in Spanish

```html
<!DOCTYPE html>
<html lang="es">
<head>
<meta charset="utf-8">
<title>Sobre ríos quietos — Marisol Quintero</title>
<link rel="stylesheet" href="https://fonts.googleapis.com/css2?family=Mr+Dafoe&family=Montserrat:wght@300;400&display=swap">
<style>
  :root {
    --page: #ffffff;
    --canyon-deep: #7e1c40;
    --canyon-mid: #a83a58;
    --canyon-warm: #c65a66;
    --canyon-light: #c97a98;
    --haze-top: #f4e6f0;
    --haze-mid: #e6bfd0;
    --grass: #d7a3b6;
    --path: #e2858f;
    --veil: #6e2350;
    --ink-light: #ffffff;
  }
  html, body {
    margin: 0;
    padding: 0;
    width: 1200px;
    height: 1000px;
    overflow: hidden;
    background: var(--page);
  }
  .canvas {
    position: relative;
    width: 1200px;
    height: 1000px;
  }
  .cover {
    position: absolute;
    left: 163px;
    top: 63px;
    width: 874px;
    height: 874px;
    overflow: hidden;
  }
  .cover-art {
    position: absolute;
    inset: 0;
    display: block;
  }
  .album-title {
    position: absolute;
    left: 0;
    right: 0;
    top: 676px;
    margin: 0;
    text-align: center;
    font-family: "Mr Dafoe", cursive;
    font-weight: 400;
    font-size: 84px;
    line-height: 1;
    color: var(--ink-light);
    white-space: nowrap;
  }
  .artist-name {
    position: absolute;
    left: 0;
    right: 0;
    top: 803px;
    margin: 0;
    text-align: center;
    font-family: "Montserrat", sans-serif;
    font-weight: 400;
    font-size: 21px;
    line-height: 1;
    letter-spacing: 0.42em;
    padding-left: 0.42em;
    color: var(--ink-light);
  }
  .title-rule {
    position: absolute;
    left: 392px;
    top: 846px;
    width: 90px;
    height: 2px;
    background: var(--ink-light);
  }
</style>
</head>
<body>
<main class="canvas">
  <section class="cover">
    <svg class="cover-art" viewBox="0 0 874 874" width="874" height="874">
      <defs>
        <linearGradient id="canyonTone" x1="0" y1="0" x2="0" y2="1">
          <stop offset="0" stop-color="var(--canyon-light)"/>
          <stop offset="0.3" stop-color="var(--canyon-warm)"/>
          <stop offset="0.6" stop-color="var(--canyon-mid)"/>
          <stop offset="0.85" stop-color="var(--canyon-deep)"/>
          <stop offset="1" stop-color="var(--canyon-warm)"/>
        </linearGradient>
        <radialGradient id="canyonShade" cx="0.5" cy="0.55" r="0.65">
          <stop offset="0" stop-color="#5a1030" stop-opacity="0.35"/>
          <stop offset="0.6" stop-color="#5a1030" stop-opacity="0.1"/>
          <stop offset="1" stop-color="#e07a80" stop-opacity="0.25"/>
        </radialGradient>
        <linearGradient id="valleyTone" x1="0" y1="0" x2="0" y2="1">
          <stop offset="0" stop-color="var(--haze-top)"/>
          <stop offset="0.3" stop-color="var(--haze-mid)"/>
          <stop offset="0.42" stop-color="#c98a9c"/>
          <stop offset="0.62" stop-color="var(--grass)"/>
          <stop offset="1" stop-color="var(--path)"/>
        </linearGradient>
        <radialGradient id="valleyLight" cx="0.5" cy="0.72" r="0.5">
          <stop offset="0" stop-color="#f0a0a4" stop-opacity="0.7"/>
          <stop offset="0.5" stop-color="#e8a6b4" stop-opacity="0.25"/>
          <stop offset="1" stop-color="#b86a86" stop-opacity="0"/>
        </radialGradient>
      </defs>
      <g class="photo-canyon" role="img" aria-label="Photograph of a red rock canyon with dry grass along a dirt path">
        <rect width="874" height="874" fill="url(#canyonTone)"/>
        <rect width="874" height="874" fill="url(#canyonShade)"/>
      </g>
      <circle class="veil-ring" cx="437" cy="410" r="470" fill="var(--veil)" opacity="0.5"/>
      <g class="photo-window" role="img" aria-label="Close view of a woman seen from behind walking along a grassy path into a hazy valley">
        <circle cx="440" cy="384" r="262" fill="url(#valleyTone)"/>
        <circle cx="440" cy="384" r="262" fill="url(#valleyLight)"/>
      </g>
    </svg>
    <h1 class="album-title">Sobre ríos quietos</h1>
    <p class="artist-name">MARISOL QUINTERO</p>
    <div class="title-rule"></div>
  </section>
</main>
</body>
</html>
```